Certified Notary Signing Agent Business Card Design

I need a modern, visually appealing two-sided business card for my mobile notary signing agent business which clearly communicates my certification by the Federal Sealwork Guild ("FSG") and Deed Closing Method ("DCM"). It should be clean and easy to read and trust focused. While I am not committed to specific fonts and colors, I do like the colors in both my final logo and a sample logo (color examples only). I want to hand out a business card that is easy to locate in a stack and differentiates itself easily from others as it is an extremely crowded market space.

Target Market(s)

Title Companies, Escrow Officers, Real Estate Agents, Real Estate Lenders

Industry/Entity Type

Real Estate Lending

Contact Information for Business Card

I need a two-sided business card for my mobile notary signing agent business that prominently displays my photo, logo (potentially, just on the back), my service areas, phone, email, url and an FSG certification and DCM certification. On the back side of the card I would like my url, logo and potentially certification icons. On the back, I MAY want to add language that I have been an FSG Certified NSA for 10 + years and have performed over 8k in real estate loan transactions. I have attached a very old biz card circa 2007 that I designed myself on a card ordering platform. While it's not great, it can display how I crammed all of the data on a single card. I am NOT suggesting replicating this design in any form but provide it as reference material only,

Font styles to use
Sans Serif

Requirements
Must have
• Name: Marla Vostrick, Certified Notary Signing Agent Phone: 936.555.0142 URL: www.PrimeQuillSigners.com Email: marla@primequillsigners.com, Counties serviced: Montgomery, Grimes, N. Harris, Walker, Waller, Federal Sealwork Guild Badge, Deed Closing Method Badge (still need to upload this)
Nice to have
• I am open to color variations on my logo as illustrated in the attachment labeled as Logo Sample Colors Only (11A) that has a slate blue/grey background w/white lettering and gold pen and circles

```html
<!DOCTYPE html>
<html lang="en">
<head>
<meta charset="utf-8">
<title>Marla Vostrick – Business Card</title>
<link rel="stylesheet" href="https://fonts.googleapis.com/css2?family=Poppins:wght@400;600&display=swap">
<style>
  :root {
    --page: #b0b0b0;
    --card: #000000;
    --gold: #e0a040;
    --white: #ffffff;
    --badge-slate: #4a5668;
    --badge-grey: #8a8f99;
    --photo-warm: #c89a72;
    --photo-deep: #6a4a30;
  }
  * { box-sizing: border-box; margin: 0; padding: 0; }
  html, body { width: 1093px; height: 1200px; overflow: hidden; }
  body {
    background: var(--page);
    font-family: "Poppins", sans-serif;
    color: var(--white);
    position: relative;
  }
  .card {
    position: absolute;
    left: 265px;
    width: 580px;
    height: 360px;
    background: var(--card);
    border-radius: 24px;
    overflow: hidden;
  }
  .card--front { top: 226px; }
  .card--back { top: 621px; }

  .portrait {
    position: absolute;
    left: 0; top: 0;
    width: 265px; height: 360px;
    background: radial-gradient(ellipse 45% 42% at 50% 46%, #e8bda0 0%, var(--photo-warm) 55%, var(--photo-deep) 100%);
  }
  .details {
    position: absolute;
    left: 292px; top: 36px;
    width: 280px;
  }
  .name {
    color: var(--gold);
    font-weight: 600;
    font-size: 20px;
    line-height: 1.15;
  }
  .title { font-size: 17px; line-height: 1.3; margin-top: 1px; }
  .rule {
    height: 1px;
    background: var(--gold);
    width: 248px;
    margin: 8px 0 11px;
  }
  .contact-list { list-style: none; }
  .contact-list li {
    display: flex; align-items: center; gap: 7px;
    font-size: 16.3px; line-height: 21px;
    white-space: nowrap;
  }
  .contact-list svg { width: 15px; height: 15px; flex: none; }
  .rule--lower { margin: 11px 0 9px; }
  .section-head {
    color: var(--gold); font-weight: 600; font-size: 19px; line-height: 1.2;
  }
  .counties { font-size: 17px; line-height: 21px; margin-top: 8px; }
  .badges {
    display: flex; align-items: center; gap: 28px;
    margin-top: 12px;
  }
  .badge { border-radius: 50%; flex: none; }
  .badge--dcm { width: 46px; height: 46px; background: var(--badge-slate); }
  .badge--fsg { width: 52px; height: 52px; background: var(--badge-grey); }

  .brand {
    position: absolute;
    left: 200px; top: 42px;
    width: 180px; height: 180px;
    border: 3px solid var(--white);
    border-radius: 50%;
    display: flex; align-items: center; justify-content: center;
    text-align: center;
    font-weight: 600; font-size: 19px; line-height: 1.25;
    text-transform: uppercase;
  }
  .back-url {
    position: absolute; left: 0; right: 0; top: 230px;
    text-align: center; color: var(--gold); font-size: 17px;
  }
  .back-rule { position: absolute; left: 26px; top: 271px; width: 529px; height: 1px; background: var(--white); }
  .credentials {
    position: absolute; left: 22px; top: 290px;
    font-size: 17.5px; line-height: 21px;
    white-space: nowrap;
  }
  .badge--back {
    position: absolute; left: 503px; top: 282px;
    width: 64px; height: 64px;
    background: var(--badge-grey);
  }
</style>
</head>
<body>
  <section class="card card--front">
    <div class="portrait" role="img" aria-label="Portrait photo of Marla Vostrick"></div>
    <div class="details">
      <h1 class="name">MARLA VOSTRICK</h1>
      <p class="title">Certified Notary Signing Agent</p>
      <div class="rule"></div>
      <ul class="contact-list">
        <li>
          <svg viewBox="0 0 24 24" fill="none" stroke="#e0a040" stroke-width="2.4"><path d="M5 3h4l2 5-2.5 1.5a11 11 0 0 0 6 6L16 13l5 2v4a2 2 0 0 1-2 2A16 16 0 0 1 3 5a2 2 0 0 1 2-2z"/></svg>
          936.555.0142
        </li>
        <li>
          <svg viewBox="0 0 24 24" fill="none" stroke="#e0a040" stroke-width="2"><circle cx="12" cy="12" r="10"/><path d="M2 12h20M12 2c3 3 3 17 0 20M12 2c-3 3-3 17 0 20"/></svg>
          www.PrimeQuillSigners.com
        </li>
        <li>
          <svg viewBox="0 0 24 24"><rect x="2" y="5" width="20" height="14" fill="#e0a040"/><path d="M2 5l10 8 10-8" fill="none" stroke="#000" stroke-width="1.6"/></svg>
          marla@primequillsigners.com
        </li>
      </ul>
      <div class="rule rule--lower"></div>
      <h2 class="section-head">COUNTIES SERVICED</h2>
      <p class="counties">Montgomery, Grimes, N. Harris,<br>Walker, Waller</p>
      <div class="badges">
        <div class="badge badge--dcm" role="img" aria-label="Deed Closing Method certification badge"></div>
        <div class="badge badge--fsg" role="img" aria-label="Federal Sealwork Guild certification badge"></div>
      </div>
    </div>
  </section>

  <section class="card card--back">
    <div class="brand">Prime Quill<br>Signing<br>Agents</div>
    <p class="back-url">www.PrimeQuillSigners.com</p>
    <div class="back-rule"></div>
    <p class="credentials">FSG Certified NSA for 10 + years and have performed<br>over 8k in real estate loan transactions.</p>
    <div class="badge badge--back" role="img" aria-label="Federal Sealwork Guild certification badge"></div>
  </section>
</body>
</html>
```